Gutschein-Design für Friseursalon gesucht
Zielgruppe
Wir sind ein Friseursalon für Jung bis Alt.
Wir bieten alles rund um das Haar an und verkaufen Haarpflegeprodukte.
Aufgabenstellung
Das Design sollte Modern und Professionell wirken.
Ebenso muss es zu unserem Firmenlogo passen.
Es sollte auf die Rückseite des Gutscheins ein Feld für den Betrag, für Wen, das Datum, den Stempel und die Gutscheinnummer vorhanden sein.

```html
<!DOCTYPE html>
<html lang="de">
<head>
<meta charset="utf-8">
<title>Gutschein – Lockenstudio by Veri</title>
<link rel="stylesheet" href="https://fonts.googleapis.com/css2?family=Barlow+Condensed:wght@400;600&family=Mrs+Saint+Delafield&display=swap">
<style>
  :root {
    --slate: #363b3f;
    --lilac: #dac6da;
    --violet: #8e1f8e;
    --ink: #2f3336;
    --white: #ffffff;
    --photo-light: #f6f3f5;
    --photo-mid: #e6e0e4;
    --photo-deep: #b9b3b7;
    --photo-accent: #c79bc9;
  }
  * { margin: 0; padding: 0; box-sizing: border-box; }
  html, body { width: 1160px; height: 1200px; overflow: hidden; background: var(--white); }
  body { position: relative; font-family: "Barlow Condensed", "Arial Narrow", sans-serif; }

  .front, .back { position: absolute; left: 0; width: 1160px; }
  .front { top: 0; height: 580px; }
  .back { top: 620px; height: 580px; background: var(--slate); }

  .front-cover { position: absolute; left: 0; top: 0; width: 589px; height: 580px; background: var(--slate); }
  .title {
    position: absolute; left: 92px; top: 108px;
    font-family: "Mrs Saint Delafield", cursive;
    font-weight: 400; color: var(--white);
    font-size: 150px; line-height: 1; white-space: nowrap;
  }
  .title-sub {
    position: absolute; left: 178px; top: 238px;
    font-family: "Mrs Saint Delafield", cursive;
    color: var(--white); font-size: 82px; line-height: 1;
  }
  .recipient-field { position: absolute; left: 21px; top: 375px; width: 547px; height: 116px; background: var(--lilac); }

  .photo {
    position: absolute;
    background:
      radial-gradient(circle at 98% 28%, var(--photo-accent) 0, var(--photo-accent) 5%, transparent 6%),
      radial-gradient(ellipse 45% 55% at 62% 48%, var(--photo-light) 0%, var(--photo-mid) 60%, transparent 100%),
      linear-gradient(160deg, var(--photo-mid) 0%, var(--photo-light) 45%, var(--photo-deep) 75%, var(--photo-light) 100%);
  }
  .front-photo { left: 589px; top: 0; width: 571px; height: 580px; }
  .back-photo { left: 45px; top: 40px; width: 498px; height: 507px; }

  .brand {
    position: absolute; display: flex; align-items: center; gap: 8px;
    font-weight: 600; color: var(--ink); white-space: nowrap;
  }
  .brand-dot { width: 10px; height: 10px; border-radius: 50%; background: var(--ink); }
  .front-photo .brand { left: 22px; top: 50px; font-size: 34px; }
  .back-photo .brand { left: 18px; top: 42px; font-size: 28px; }

  .salon-contact { position: absolute; left: 198px; top: 370px; color: var(--ink); font-weight: 600; font-size: 20px; line-height: 23px; }
  .salon-owner { color: var(--violet); font-size: 24px; line-height: 26px; margin-bottom: 1px; }
  .salon-role { margin-bottom: 6px; }

  .field { position: absolute; left: 587px; width: 546px; background: var(--lilac); }
  .field-amount { top: 39px; height: 80px; }
  .field-words { top: 158px; height: 79px; }
  .field-stamp { top: 280px; height: 155px; }
  .field-number { top: 501px; height: 47px; }
  .field-label { position: absolute; left: 596px; color: var(--white); font-size: 21px; font-weight: 400; }
  .label-amount { top: 122px; }
  .label-words { top: 241px; }
  .label-stamp { top: 440px; }
  .field-number span { position: absolute; left: 11px; top: 11px; font-size: 21px; color: var(--ink); }
</style>
</head>
<body>
  <section class="front">
    <div class="front-cover">
      <div class="title">Gutschein</div>
      <div class="title-sub">für</div>
      <div class="recipient-field"></div>
    </div>
    <div class="photo front-photo" role="img" aria-label="Schwarzweiß-Porträt einer Frau mit langem, lockigem blondem Haar, violettem Augen-Make-up und violettem Armreif">
      <div class="brand"><span class="brand-dot"></span>Lockenstudio by Veri</div>
    </div>
  </section>

  <section class="back">
    <div class="photo back-photo" role="img" aria-label="Schwarzweiß-Porträt einer Frau mit langem, lockigem blondem Haar, violettem Augen-Make-up und violettem Armreif">
      <div class="brand"><span class="brand-dot"></span>Lockenstudio by Veri</div>
      <div class="salon-contact">
        <div class="salon-owner">Veri Sonnfeld</div>
        <div class="salon-role">Inhaberin / Friseurmeisterin</div>
        <div>Lindenweg 8</div>
        <div>54329 Tannwald</div>
        <div>Telefon: 06571/4820</div>
      </div>
    </div>

    <div class="field field-amount"></div>
    <div class="field-label label-amount">Betrag / €</div>
    <div class="field field-words"></div>
    <div class="field-label label-words">Betrag in Worten</div>
    <div class="field field-stamp"></div>
    <div class="field-label label-stamp">Datum / Stempel</div>
    <div class="field field-number"><span>Gutschein-Nr.</span></div>
  </section>
</body>
</html>
```